Retractable Banners Designs for Tradeshows

We like the look and feel of the banners draft but want a more polished and improved version of the banners

The dimensions of each banner should be 33" x 80"

We want the banners to work on their own as they will be used in different places, but at tradeshows, they might be used side by side in a 10x10 tradeshow booth, so common design elements that work together is needed.
Updates

Low design quality

Target Market(s)

tradeshows booths

Colors
EB3D1F
EC4F4E
F09395
F8D3D4
FCEDEE

Requirements
Must have
• Elements that tie all the banners together, large scale images, not to cluttered or busy, designed to be visible and attractive from far away, our corporate colours are red, black, white and gray
Nice to have
• bright design not dark but using our corporate colours of red, gray, white and some black

```html
<!DOCTYPE html>
<html lang="en">
<head>
<meta charset="utf-8">
<title>NordWave Tradeshow Banners</title>
<link href="https://fonts.googleapis.com/css2?family=Barlow+Condensed:wght@700&family=Barlow:wght@500;700&display=swap" rel="stylesheet">
<style>
  :root {
    --red: #ec1c24;
    --black: #000000;
    --white: #ffffff;
    --sky-deep: #2a68d6;
    --sky-mid: #4a88e6;
    --sky-pale: #7fb0f0;
    --steel-pale: #d9dde3;
    --rack-dark: #1f2a36;
    --rack-mid: #4a5e74;
    --rack-light: #9aa8b8;
    --cable-yellow: #d8c24a;
    --lab-dark: #2e2e30;
    --lab-mid: #6d6b68;
    --lab-light: #cfcdc8;
    --probe-orange: #e07a22;
    --site-dark: #3e3a36;
    --site-mid: #7d7468;
    --site-light: #c4b8a6;
    --shirt-red: #9a3a36;
  }
  * { margin: 0; padding: 0; box-sizing: border-box; }
  html, body { width: 1200px; height: 720px; overflow: hidden; background: var(--white); }
  .stage { position: relative; width: 1200px; height: 720px; }
  .banner {
    position: absolute; top: 75px; width: 234px; height: 568px; overflow: hidden;
    box-shadow: 0 6px 18px rgba(0,0,0,0.28);
    font-family: "Barlow", sans-serif;
  }
  .banner--telecom { left: 61px; }
  .banner--ict { left: 339px; }
  .banner--test { left: 616px; }
  .banner--hardware { left: 893px; }
  .banner__art { position: absolute; inset: 0; width: 234px; height: 568px; display: block; }
  .brand {
    position: absolute; top: 56px; left: 0; width: 100%;
    display: flex; align-items: center; justify-content: center; gap: 8px;
    font-family: "Barlow", sans-serif; font-weight: 500; font-size: 31px; letter-spacing: -0.5px;
  }
  .brand__dot { width: 11px; height: 11px; border-radius: 50%; background: var(--red); }
  .banner--dark .brand { color: var(--white); }
  .banner--light .brand { color: var(--black); }
  .copy { position: absolute; left: 33px; right: 12px; color: var(--white); }
  .copy--two-line { top: 385px; }
  .copy--one-line { top: 401px; }
  .headline {
    font-family: "Barlow Condensed", sans-serif; font-weight: 700;
    font-size: 27px; line-height: 27.5px; text-transform: uppercase; letter-spacing: 0.2px;
  }
  .tagline { margin-top: 10px; font-size: 12.5px; line-height: 17.5px; font-weight: 500; }
  .copy--one-line .tagline { margin-top: 8px; }
  .url {
    position: absolute; left: 33px; top: 512px; color: var(--white);
    font-size: 12px; letter-spacing: 3.6px; font-weight: 500; white-space: nowrap;
  }
  .url b { font-weight: 700; }
</style>
</head>
<body>
<div class="stage">

  <section class="banner banner--dark banner--telecom">
    <svg class="banner__art" viewBox="0 0 234 568">
      <defs>
        <linearGradient id="skyBase" x1="0" y1="0" x2="0" y2="1">
          <stop offset="0" stop-color="var(--sky-deep)"/>
          <stop offset="0.6" stop-color="var(--sky-mid)"/>
          <stop offset="1" stop-color="var(--sky-pale)"/>
        </linearGradient>
        <radialGradient id="skyGlow" cx="0.5" cy="0.55" r="0.45">
          <stop offset="0" stop-color="var(--steel-pale)" stop-opacity="0.55"/>
          <stop offset="1" stop-color="var(--steel-pale)" stop-opacity="0"/>
        </radialGradient>
      </defs>
      <rect width="234" height="568" fill="var(--black)"/>
      <g role="img" aria-label="Photo of a cellular tower with antennas against a blue sky">
        <polygon points="0,136 234,82 234,352 156,375 0,329" fill="url(#skyBase)"/>
        <polygon points="0,136 234,82 234,352 156,375 0,329" fill="url(#skyGlow)"/>
      </g>
      <polygon points="234,352 234,399 156,375" fill="var(--red)"/>
      <rect y="501" width="234" height="67" fill="var(--red)"/>
      <polygon points="0,542 0,568 96,568" fill="var(--black)"/>
    </svg>
    <div class="brand"><span class="brand__dot"></span>nordwave</div>
    <div class="copy copy--two-line">
      <h2 class="headline">Telecom<br>Infrastructure</h2>
      <p class="tagline">Cutting Edge Solutions<br>for the Next Generation</p>
    </div>
    <p class="url">www.<b>NordWave</b>.com</p>
  </section>

  <section class="banner banner--light banner--ict">
    <svg class="banner__art" viewBox="0 0 234 568">
      <defs>
        <linearGradient id="rackBase" x1="0" y1="0" x2="1" y2="0.6">
          <stop offset="0" stop-color="var(--rack-mid)"/>
          <stop offset="0.35" stop-color="var(--rack-dark)"/>
          <stop offset="0.7" stop-color="var(--rack-mid)"/>
          <stop offset="1" stop-color="var(--rack-light)"/>
        </linearGradient>
        <radialGradient id="rackCable" cx="0.55" cy="0.95" r="0.35">
          <stop offset="0" stop-color="var(--cable-yellow)" stop-opacity="0.45"/>
          <stop offset="1" stop-color="var(--cable-yellow)" stop-opacity="0"/>
        </radialGradient>
      </defs>
      <rect width="234" height="568" fill="var(--white)"/>
      <rect y="320" width="234" height="181" fill="var(--red)"/>
      <g role="img" aria-label="Photo of server racks with network equipment and fibre cabling">
        <polygon points="0,136 234,82 234,352 156,375 0,329" fill="url(#rackBase)"/>
        <polygon points="0,136 234,82 234,352 156,375 0,329" fill="url(#rackCable)"/>
      </g>
      <polygon points="234,352 234,399 156,375" fill="var(--black)"/>
      <rect y="501" width="234" height="67" fill="var(--black)"/>
      <polygon points="0,542 0,568 96,568" fill="var(--red)"/>
    </svg>
    <div class="brand"><span class="brand__dot"></span>nordwave</div>
    <div class="copy copy--one-line">
      <h2 class="headline">ICT Solutions</h2>
      <p class="tagline">Seemless Cable<br>and Telecom Networks and<br>Enterprise Deployments</p>
    </div>
    <p class="url">www.<b>NordWave</b>.com</p>
  </section>

  <section class="banner banner--dark banner--test">
    <svg class="banner__art" viewBox="0 0 234 568">
      <defs>
        <linearGradient id="labBase" x1="0" y1="0" x2="0" y2="1">
          <stop offset="0" stop-color="var(--lab-dark)"/>
          <stop offset="0.3" stop-color="var(--lab-light)"/>
          <stop offset="0.55" stop-color="var(--lab-mid)"/>
          <stop offset="0.8" stop-color="var(--lab-dark)"/>
          <stop offset="1" stop-color="var(--lab-light)"/>
        </linearGradient>
        <radialGradient id="labProbe" cx="0.72" cy="0.8" r="0.2">
          <stop offset="0" stop-color="var(--probe-orange)" stop-opacity="0.5"/>
          <stop offset="1" stop-color="var(--probe-orange)" stop-opacity="0"/>
        </radialGradient>
      </defs>
      <rect width="234" height="568" fill="var(--black)"/>
      <g role="img" aria-label="Photo of test instruments, oscilloscopes and multimeters on lab shelves">
        <polygon points="0,136 234,82 234,352 156,375 0,329" fill="url(#labBase)"/>
        <polygon points="0,136 234,82 234,352 156,375 0,329" fill="url(#labProbe)"/>
      </g>
      <polygon points="234,352 234,399 156,375" fill="var(--red)"/>
      <rect y="501" width="234" height="67" fill="var(--red)"/>
      <polygon points="0,542 0,568 96,568" fill="var(--black)"/>
    </svg>
    <div class="brand"><span class="brand__dot"></span>nordwave</div>
    <div class="copy copy--two-line">
      <h2 class="headline">Test &amp;<br>Measurement</h2>
      <p class="tagline">Accurate and Efficient Solutions<br>for the Wireless World</p>
    </div>
    <p class="url">www.<b>NordWave</b>.com</p>
  </section>

  <section class="banner banner--light banner--hardware">
    <svg class="banner__art" viewBox="0 0 234 568">
      <defs>
        <linearGradient id="siteBase" x1="0" y1="0" x2="1" y2="0.4">
          <stop offset="0" stop-color="var(--site-mid)"/>
          <stop offset="0.35" stop-color="var(--site-dark)"/>
          <stop offset="0.7" stop-color="var(--site-mid)"/>
          <stop offset="1" stop-color="var(--site-light)"/>
        </linearGradient>
        <radialGradient id="siteWorker" cx="0.78" cy="0.4" r="0.3">
          <stop offset="0" stop-color="var(--shirt-red)" stop-opacity="0.5"/>
          <stop offset="1" stop-color="var(--shirt-red)" stop-opacity="0"/>
        </radialGradient>
      </defs>
      <rect width="234" height="568" fill="var(--white)"/>
      <rect y="320" width="234" height="181" fill="var(--red)"/>
      <g role="img" aria-label="Photo of a technician in a hard hat working on rooftop radio equipment">
        <polygon points="0,136 234,82 234,352 156,375 0,329" fill="url(#siteBase)"/>
        <polygon points="0,136 234,82 234,352 156,375 0,329" fill="url(#siteWorker)"/>
      </g>
      <polygon points="234,352 234,399 156,375" fill="var(--black)"/>
      <rect y="501" width="234" height="67" fill="var(--black)"/>
      <polygon points="0,542 0,568 96,568" fill="var(--red)"/>
    </svg>
    <div class="brand"><span class="brand__dot"></span>nordwave</div>
    <div class="copy copy--one-line">
      <h2 class="headline">Hardware</h2>
      <p class="tagline">High-Quality, Economical,<br>Test Grade RF and Microwave<br>Components</p>
    </div>
    <p class="url">www.<b>NordWave</b>.com</p>
  </section>

</div>
</body>
</html>
```